Business Cards for accounting firm

Need a file and design that we can update for our employees when we get a design we like. Logo is attached.
Megan Tolliver CPA
Owner
P.O. Box 418
Perrysburg OH 43187
4193628405
megan@brightlanefin.com
www.brightlanefin.com
Accounting

```html
<!DOCTYPE html>
<html lang="en">
<head>
<meta charset="UTF-8">
<title>Brightlane Financial – Business Card</title>
<link rel="stylesheet" href="https://fonts.googleapis.com/css2?family=Open+Sans:wght@400;600&family=Exo+2:wght@400&family=Tinos&display=swap">
<style>
  :root {
    --backdrop: #d9d9d9;
    --card: #f4f4f3;
    --accent: #1f9fd8;
    --ink: #4a4a4a;
  }
  * { margin: 0; padding: 0; box-sizing: border-box; }
  html, body {
    width: 1200px;
    height: 900px;
    overflow: hidden;
    background: var(--backdrop);
  }
  .canvas {
    position: relative;
    width: 1200px;
    height: 900px;
  }
  .card {
    position: absolute;
    width: 560px;
    height: 320px;
    background: var(--card);
    box-shadow: 0 6px 18px rgba(0, 0, 0, 0.12);
  }
  /* Front: name and contact */
  .card--front { left: 590px; top: 130px; }
  .accent-bar {
    position: absolute;
    left: 150px;
    top: 0;
    width: 36px;
    height: 130px;
    background: var(--accent);
  }
  .person-name {
    position: absolute;
    left: 86px;
    top: 140px;
    font-family: "Open Sans", sans-serif;
    font-weight: 400;
    font-size: 31px;
    color: var(--ink);
    letter-spacing: -0.3px;
    white-space: nowrap;
  }
  .person-role {
    position: absolute;
    left: 88px;
    top: 184px;
    font-family: "Exo 2", sans-serif;
    font-size: 13px;
    color: var(--accent);
  }
  .contact {
    position: absolute;
    right: 40px;
    bottom: 30px;
    font-family: "Tinos", serif;
    font-size: 13px;
    line-height: 15px;
    color: var(--accent);
    list-style: none;
    white-space: nowrap;
  }
  /* Back: company name */
  .card--back { left: 80px; top: 440px; }
  .company-name {
    position: absolute;
    right: 36px;
    bottom: 40px;
    font-family: "Open Sans", sans-serif;
    font-weight: 600;
    font-size: 34px;
    line-height: 1.05;
    color: var(--accent);
    text-align: right;
  }
</style>
</head>
<body>
  <main class="canvas">
    <section class="card card--front" aria-label="Business card front">
      <div class="accent-bar"></div>
      <h1 class="person-name">Megan Tolliver CPA</h1>
      <p class="person-role">Owner</p>
      <ul class="contact">
        <li>P.O. Box 418</li>
        <li>Millbrook Vale 43187</li>
        <li>5553628405</li>
        <li>megan@brightlanefin.com</li>
        <li>www.brightlanefin.com</li>
      </ul>
    </section>

    <section class="card card--back" aria-label="Business card back">
      <p class="company-name">Brightlane<br>Financial</p>
    </section>
  </main>
</body>
</html>
```